Healthy Supplement featuring Moringa products

Need 3 business card options for our reps to order from Cardloom. Our reps will be ordering from Cardloom once we upload them. Attached is our current designs to show what info needs to be on the cards. Our website is www.tkvitality.com
The business cards will be a template for our reps to order from. Most of our reps are Asian & Hispanic. Please look at our website so you can see who we are to get the look and feel what we need.
Target Market(s)
Adults 30 on up. Health oriented people.
Industry/Entity Type
Health And Wellness
Contact Information for Business Card
Name
Title
Phone
Logo
www.tkvitality.com/my/username
Font styles to use
Requirements
Must have
- Please match our website look and colors. A moringa leaf is nice, but am open to something different.
Nice to have
- Healthy looking and warm, not super cold or too modern.
Should not have
- No harsh colors please.

```html
<!DOCTYPE html>
<html lang="en">
<head>
<meta charset="utf-8">
<title>TK Vitality – Business Card</title>
<link rel="stylesheet" href="https://fonts.googleapis.com/css2?family=Marcellus&family=PT+Sans:ital,wght@0,400;1,400&display=swap">
<style>
  :root {
    --canvas: #e9e7e2;
    --charcoal: #3e3e40;
    --charcoal-deep: #323234;
    --leaf: #6aaa3e;
    --leaf-bright: #8cc63f;
    --leaf-soft: #7fbf4d;
    --paper: #ffffff;
    --ink: #2b2b2b;
  }
  * { box-sizing: border-box; margin: 0; padding: 0; }
  html, body { width: 1200px; height: 900px; overflow: hidden; }
  body {
    background: var(--canvas);
    font-family: "PT Sans", sans-serif;
    position: relative;
  }
  .card {
    position: absolute;
    left: 250px;
    width: 700px;
    height: 400px;
    overflow: hidden;
    box-shadow: 0 6px 18px rgba(0,0,0,0.22);
  }
  .card-back { top: 35px; background: var(--charcoal); }
  .card-front { top: 470px; background: var(--charcoal); }

  /* Back */
  .back-brand {
    position: absolute;
    top: 130px;
    left: 0;
    width: 100%;
    display: flex;
    justify-content: center;
    align-items: center;
    gap: 16px;
  }
  .brand-dot {
    width: 40px; height: 40px;
    border-radius: 50%;
    background: var(--leaf-bright);
  }
  .brand-name {
    font-family: "Marcellus", serif;
    color: var(--leaf-bright);
    letter-spacing: 0.12em;
    text-transform: uppercase;
  }
  .back-brand .brand-name { font-size: 46px; }
  .back-rule {
    position: absolute;
    left: 0; top: 292px;
    width: 100%;
    display: flex;
    align-items: center;
    gap: 14px;
    padding-left: 250px;
  }
  .back-url {
    font-family: "Marcellus", serif;
    color: var(--leaf-bright);
    font-size: 17px;
    letter-spacing: 0.14em;
    text-transform: uppercase;
    white-space: nowrap;
  }
  .back-line { flex: 1; height: 3px; background: var(--leaf-bright); }

  /* Front */
  .front-shapes { position: absolute; inset: 0; }
  .front-name {
    position: absolute;
    left: 240px; top: 42px;
    font-family: "Marcellus", serif;
    font-size: 25px;
    letter-spacing: 0.06em;
    color: var(--ink);
  }
  .front-title {
    position: absolute;
    left: 238px; top: 74px;
    right: 0;
    display: flex;
    align-items: center;
    gap: 8px;
  }
  .front-title span {
    font-size: 20px;
    color: var(--leaf);
    white-space: nowrap;
  }
  .title-line { flex: 1; height: 2px; background: var(--leaf-bright); }
  .contact-list {
    position: absolute;
    left: 215px; top: 150px;
    list-style: none;
  }
  .contact-list li {
    display: flex;
    align-items: center;
    gap: 14px;
    height: 36px;
    font-size: 20px;
    color: var(--ink);
  }
  .contact-icon {
    width: 24px; height: 24px;
    border-radius: 50%;
    background: var(--leaf);
    display: flex; align-items: center; justify-content: center;
  }
  .front-brand {
    position: absolute;
    right: 50px; top: 205px;
    display: flex;
    align-items: center;
    gap: 10px;
  }
  .front-brand .brand-dot { width: 26px; height: 26px; }
  .front-brand .brand-name { font-size: 24px; color: var(--leaf); }
  .front-brand .brand-dot { background: var(--leaf); }
</style>
</head>
<body>

<section class="card card-back" aria-label="Card back">
  <div class="back-brand">
    <span class="brand-dot"></span>
    <span class="brand-name">TK Vitality</span>
  </div>
  <div class="back-rule">
    <span class="back-url">www.tkvitality.com</span>
    <span class="back-line"></span>
  </div>
</section>

<section class="card card-front" aria-label="Card front">
  <svg class="front-shapes" viewBox="0 0 700 400" width="700" height="400" aria-hidden="true">
    <defs>
      <linearGradient id="greenSweep" x1="0" y1="0" x2="1" y2="0">
        <stop offset="0" stop-color="#64a83a"/>
        <stop offset="1" stop-color="#7dbd4c"/>
      </linearGradient>
    </defs>
    <rect width="700" height="400" fill="#3e3e40"/>
    <path d="M0 0 H700 V312 C520 340 260 365 0 255 Z" fill="url(#greenSweep)"/>
    <path d="M0 255 C260 365 520 340 700 312" fill="none" stroke="#8cc63f" stroke-width="4"/>
    <path d="M206 0 H700 V292 C540 318 330 322 250 282 C185 248 168 130 206 0 Z" fill="#8cc63f"/>
    <path d="M216 0 H700 V284 C540 310 335 314 256 276 C196 244 180 130 216 0 Z" fill="#ffffff"/>
  </svg>
  <svg style="position:absolute;left:70px;top:150px" width="170" height="180" viewBox="0 0 170 180" role="img" aria-label="Faint moringa leaf sprig decoration">
    <ellipse cx="85" cy="90" rx="80" ry="85" fill="#8cc63f" opacity="0.25"/>
  </svg>

  <div class="front-name">YOUR NAME</div>
  <div class="front-title"><span>Job Title</span><span class="title-line"></span></div>

  <ul class="contact-list">
    <li>
      <span class="contact-icon">
        <svg width="14" height="14" viewBox="0 0 14 14" aria-hidden="true"><path d="M2 5 Q7 1 12 5 L10 6 Q7 4 4 6 Z M4 7 H10 L11 12 H3 Z" fill="#fff"/></svg>
      </span>000 000 0000
    </li>
    <li>
      <span class="contact-icon">
        <svg width="14" height="14" viewBox="0 0 14 14" aria-hidden="true"><rect x="1.5" y="3.5" width="11" height="7" fill="none" stroke="#fff" stroke-width="1.4"/><path d="M1.5 3.5 L7 8 L12.5 3.5" fill="none" stroke="#fff" stroke-width="1.4"/></svg>
      </span>youremail@xyz.com
    </li>
    <li>
      <span class="contact-icon">
        <svg width="14" height="14" viewBox="0 0 14 14" aria-hidden="true"><circle cx="7" cy="7" r="5.5" fill="none" stroke="#fff" stroke-width="1.2"/><ellipse cx="7" cy="7" rx="2.4" ry="5.5" fill="none" stroke="#fff" stroke-width="1"/><path d="M1.5 7 H12.5" stroke="#fff" stroke-width="1"/></svg>
      </span>www.tkvitality.com
    </li>
  </ul>

  <div class="front-brand">
    <span class="brand-dot"></span>
    <span class="brand-name">TK Vitality</span>
  </div>
</section>

</body>
</html>
```